MyRiverbendGroove Web Site Header

Potential designers can visit the site (MyRiverbendGroove.com) to see our current header. The orange color CANNOT CHANGE! Please do not submit anything different colors. The header needs to contain the following items:
-MyRiverbendGroove.com
-Catch Every Single Beat (There IS NO "?" BEHIND THIS!)
- 404.582.3967

I've supplied 13 different photos that you can choose from as a background.

Images of 920 x 150 pixels are the "exact size" that will fit my site. If it's larger, and I have to crop on uploading, I could lose text along the edges. (for what that info is worth!)

Background: Midtown Atlanta is the urban living core of Atlanta. Filled with highrise condominiums, restaurants, shopping and is also called the Heart of the Arts because Lark Playhouse and Crane Gallery are located there. It's a diverse mixture of people that live there, as well as all the office buildings that are filled daily.

The final design should give a feel of excitement, hence our tagline, Catch Every Single Beat.
Updates

Project Deadline Extended
Reason: I've gotten some INCREDIBLE designs. It's been hard to make a decision. In fact, may have to select more than one. I'm also in the middle of another project and have been swamped with it.

Target Market(s)

Target market is condo buyers. Age range from 20's to 50's. Heavy concentration of law offices and high-tech companies in the area...so think techy consumer.

Industry/Entity Type

Shopping

Font styles to use
Sans Serif

Colors
f37022

Requirements
Must have
• Phone Number 404.582.3967 or 404-582-3967

MyRiverbendGroove.com site name in header

```html
<!DOCTYPE html>
<html lang="en">
<head>
<meta charset="utf-8">
<title>MyRiverbendGroove Header Set</title>
<link rel="stylesheet" href="https://fonts.googleapis.com/css2?family=Nunito:wght@300;400;600;700;800&display=swap">
<style>
  :root {
    --brand-orange: #f37022;
    --ink: #2b2b2b;
    --canvas: #ffffff;
    --panel: #f6f6f6;
    --rule: #d9d9d9;
    --shadow: rgba(0, 0, 0, 0.18);
  }
  * { box-sizing: border-box; margin: 0; padding: 0; }
  html, body {
    width: 1200px;
    height: 800px;
    overflow: hidden;
    background: var(--canvas);
    font-family: "Nunito", sans-serif;
  }
  .header-set {
    position: relative;
    width: 1200px;
    height: 800px;
  }
  .banner {
    position: absolute;
    left: 106px;
    width: 1012px;
    height: 165px;
    background: var(--panel);
    box-shadow: 0 1px 5px var(--shadow);
    overflow: hidden;
  }
  .banner--pool { top: 12px; }
  .banner--lounge { top: 216px; --photo-top: 612px; --photo-bottom: 454px; --text-x: 780px; }
  .banner--tower { top: 412px; --photo-top: 556px; --photo-bottom: 394px; }
  .banner--garden { top: 608px; }

  .banner__photo {
    position: absolute;
    inset: 0;
    clip-path: polygon(0 0, var(--photo-top, 554px) 0, var(--photo-bottom, 399px) 100%, 0 100%);
  }
  .banner__edge {
    position: absolute;
    inset: 0;
    width: 100%;
    height: 100%;
  }
  .photo-pool { background: linear-gradient(160deg, #5b6470 0%, #7fb8d8 38%, #4aa3d6 55%, #c9c0b2 80%, #a89d8e 100%); }
  .photo-lounge { background: linear-gradient(110deg, #6a6a6e 0%, #8f6d8f 30%, #d9d9dc 52%, #6b6a70 72%, #a2568f 100%); }
  .photo-tower { background: linear-gradient(100deg, #5c8a3e 0%, #7aa7d6 30%, #b8c6d2 55%, #4f86c4 80%, #6b9fd6 100%); }
  .photo-garden { background: linear-gradient(180deg, #b7d2ea 0%, #8aa9b8 30%, #4f7a3a 60%, #7fc8e8 90%, #a9dcf0 100%); }

  .banner__text {
    position: absolute;
    top: 36px;
    left: var(--text-x, 756px);
    transform: translateX(-50%);
    text-align: center;
    white-space: nowrap;
  }
  .site-name {
    color: var(--brand-orange);
    font-size: 25px;
    font-weight: 600;
    line-height: 30px;
    letter-spacing: 0.2px;
  }
  .tagline {
    margin-top: 4px;
    color: var(--ink);
    font-size: 31px;
    font-weight: 300;
    line-height: 36px;
  }
  .tagline__strong { font-weight: 700; }

  .phone {
    position: absolute;
    right: 10px;
    bottom: 9px;
    display: flex;
    align-items: center;
    gap: 7px;
    color: var(--ink);
    font-size: 19px;
    font-weight: 700;
  }
  .phone__icon { width: 18px; height: 18px; display: block; }
</style>
</head>
<body>
<main class="header-set">

  <section class="banner banner--pool">
    <div class="banner__photo photo-pool" role="img" aria-label="Rooftop pool deck with lounge chairs beside a lap pool"></div>
    <svg class="banner__edge" viewBox="0 0 1012 165" aria-hidden="true"><line x1="566" y1="0" x2="411" y2="165" stroke="var(--rule)" stroke-width="1.5"/></svg>
    <div class="banner__text">
      <p class="site-name">MyRiverbendGroove.com</p>
      <p class="tagline">Catch Every <span class="tagline__strong">Single Beat</span></p>
    </div>
    <p class="phone"><svg class="phone__icon" viewBox="0 0 18 18" aria-hidden="true"><rect width="18" height="18" rx="3" fill="var(--brand-orange)"/><path d="M6 4.5c.6 0 1.3 1.7 1.3 2.3 0 .6-.9.8-.9 1.3 0 .9 1.6 2.8 2.6 2.8.5 0 .7-.9 1.3-.9.6 0 2.3.7 2.3 1.3 0 1-1.3 2.3-2.3 2.3C7.6 13.6 4.4 10.4 4.4 7.7c0-1.2 1-3.2 1.6-3.2z" fill="#fff"/></svg>404-582-3967</p>
  </section>

  <section class="banner banner--lounge">
    <div class="banner__photo photo-lounge" role="img" aria-label="Lounge area with striped cushioned chairs around a small round table"></div>
    <svg class="banner__edge" viewBox="0 0 1012 165" aria-hidden="true"><line x1="624" y1="0" x2="466" y2="165" stroke="var(--rule)" stroke-width="1.5"/></svg>
    <div class="banner__text">
      <p class="site-name">MyRiverbendGroove.com</p>
      <p class="tagline">Catch Every <span class="tagline__strong">Single Beat</span></p>
    </div>
    <p class="phone"><svg class="phone__icon" viewBox="0 0 18 18" aria-hidden="true"><rect width="18" height="18" rx="3" fill="var(--brand-orange)"/><path d="M6 4.5c.6 0 1.3 1.7 1.3 2.3 0 .6-.9.8-.9 1.3 0 .9 1.6 2.8 2.6 2.8.5 0 .7-.9 1.3-.9.6 0 2.3.7 2.3 1.3 0 1-1.3 2.3-2.3 2.3C7.6 13.6 4.4 10.4 4.4 7.7c0-1.2 1-3.2 1.6-3.2z" fill="#fff"/></svg>404-582-3967</p>
  </section>

  <section class="banner banner--tower">
    <div class="banner__photo photo-tower" role="img" aria-label="Glass highrise condominium tower against a blue sky with trees in front"></div>
    <svg class="banner__edge" viewBox="0 0 1012 165" aria-hidden="true"><line x1="568" y1="0" x2="406" y2="165" stroke="var(--rule)" stroke-width="1.5"/></svg>
    <div class="banner__text">
      <p class="site-name">MyRiverbendGroove.com</p>
      <p class="tagline">Catch Every <span class="tagline__strong">Single Beat</span></p>
    </div>
    <p class="phone"><svg class="phone__icon" viewBox="0 0 18 18" aria-hidden="true"><rect width="18" height="18" rx="3" fill="var(--brand-orange)"/><path d="M6 4.5c.6 0 1.3 1.7 1.3 2.3 0 .6-.9.8-.9 1.3 0 .9 1.6 2.8 2.6 2.8.5 0 .7-.9 1.3-.9.6 0 2.3.7 2.3 1.3 0 1-1.3 2.3-2.3 2.3C7.6 13.6 4.4 10.4 4.4 7.7c0-1.2 1-3.2 1.6-3.2z" fill="#fff"/></svg>404-582-3967</p>
  </section>

  <section class="banner banner--garden">
    <div class="banner__photo photo-garden" role="img" aria-label="Landscaped terrace with pergola, trees and pool below a glass residential building"></div>
    <svg class="banner__edge" viewBox="0 0 1012 165" aria-hidden="true"><line x1="566" y1="0" x2="411" y2="165" stroke="var(--rule)" stroke-width="1.5"/></svg>
    <div class="banner__text">
      <p class="site-name">MyRiverbendGroove.com</p>
      <p class="tagline">Catch Every <span class="tagline__strong">Single Beat</span></p>
    </div>
    <p class="phone"><svg class="phone__icon" viewBox="0 0 18 18" aria-hidden="true"><rect width="18" height="18" rx="3" fill="var(--brand-orange)"/><path d="M6 4.5c.6 0 1.3 1.7 1.3 2.3 0 .6-.9.8-.9 1.3 0 .9 1.6 2.8 2.6 2.8.5 0 .7-.9 1.3-.9.6 0 2.3.7 2.3 1.3 0 1-1.3 2.3-2.3 2.3C7.6 13.6 4.4 10.4 4.4 7.7c0-1.2 1-3.2 1.6-3.2z" fill="#fff"/></svg>404-582-3967</p>
  </section>

</main>
</body>
</html>
```